Heron Freightlines needs Bussiness cards!

Our new trucking company needs business cards!
We need the same design with two different names and emails, everything else it's the same.
I have included our original logo so we can use it for the design.
Note: the logo to be used is the o e with the buffalo on the right side, next to the letters H and F.

Target Market(s)

Trucking, refrigerated transportation, freight

Industry/Entity Type

Business

Contact Information for Business Card

Card #1:
Marcus Tellwright
marcustellwright@heronfreightlines.example
1-844-555-0193
(956)555-0178
3817 W. Tarrow Ave.
Pharr, TX 78599
www.heronfreightlines.example

Card#2:
Orla Brennick
orla@heronfreightlines.example
1-844-555-0193
(956)555-0178
3817 W. Tarrow Ave.
Pharr, TX 78599
www.heronfreightlines.example

Font styles to use
Sans Serif

Colors
0655a3
ec1f27
ffffff

Requirements
Must have
• our logo
Nice to have
• roads on background,

```html
<!DOCTYPE html>
<html lang="en">
<head>
<meta charset="utf-8">
<title>Heron Freightlines Business Card</title>
<link href="https://fonts.googleapis.com/css2?family=Open+Sans:wght@400;600;700;800&display=swap" rel="stylesheet">
<style>
  :root {
    --brand-blue: #0655a3;
    --brand-navy: #0b2f6b;
    --brand-red: #ec1f27;
    --paper: #f6f6f6;
    --white: #ffffff;
    --stage: #e4e6ea;
  }
  * { box-sizing: border-box; margin: 0; padding: 0; }
  html, body { width: 1200px; height: 900px; overflow: hidden; }
  body {
    background: var(--stage);
    font-family: "Open Sans", Arial, sans-serif;
    display: flex; flex-direction: column; align-items: center; justify-content: center;
    gap: 56px;
  }
  .card {
    position: relative;
    width: 600px; height: 343px;
    border-radius: 26px;
    overflow: hidden;
    box-shadow: 0 10px 28px rgba(0,0,0,0.18);
  }
  .card-front { background: var(--paper); }
  .front-wave { position: absolute; inset: 0; width: 100%; height: 100%; }
  .wordmark {
    display: flex; align-items: center; gap: 10px;
    font-weight: 800; letter-spacing: 0.01em;
  }
  .wordmark-dot { width: 14px; height: 14px; border-radius: 50%; background: var(--brand-red); }
  .card-front .wordmark {
    position: absolute; left: 34px; top: 30px;
    font-size: 26px; color: var(--brand-navy);
  }
  .holder-name {
    position: absolute; right: 40px; top: 96px;
    font-size: 26px; font-weight: 700; color: var(--brand-navy);
  }
  .address {
    position: absolute; left: 28px; bottom: 20px;
    font-size: 11.5px; color: var(--white);
  }
  .contact-list {
    position: absolute; right: 24px; bottom: 16px;
    list-style: none;
    display: flex; flex-direction: column; gap: 4px;
  }
  .contact-item {
    display: flex; align-items: center; justify-content: flex-end; gap: 8px;
    font-size: 12px; color: var(--white);
  }
  .contact-icon { width: 16px; height: 16px; flex: none; }
  .card-back {
    background: var(--brand-blue);
    display: flex; flex-direction: column; align-items: center; justify-content: center;
    gap: 22px;
  }
  .card-back .wordmark { font-size: 40px; color: var(--white); }
  .card-back .wordmark-dot { width: 20px; height: 20px; }
  .back-web {
    font-size: 13px; letter-spacing: 0.18em; color: var(--white);
  }
</style>
</head>
<body>

<section class="card card-front" aria-label="Business card front">
  <svg class="front-wave" viewBox="0 0 600 343" preserveAspectRatio="none" aria-hidden="true">
    <path d="M0,80 C170,80 330,182 600,192 L600,343 L0,343 Z" fill="var(--brand-red)"/>
    <path d="M0,92 C170,92 330,194 600,204 L600,343 L0,343 Z" fill="var(--paper)"/>
    <path d="M0,98 C170,98 330,200 600,210 L600,343 L0,343 Z" fill="var(--brand-blue)"/>
  </svg>

  <div class="wordmark"><span class="wordmark-dot"></span>Heron Freightlines</div>
  <h1 class="holder-name">Marcus Tellwright</h1>
  <p class="address">3817 W. Tarrow Ave. Pharr, TX 78599</p>

  <ul class="contact-list">
    <li class="contact-item">1-844-555-0193
      <svg class="contact-icon" viewBox="0 0 16 16"><circle cx="8" cy="8" r="7" fill="none" stroke="#fff" stroke-width="1.2"/><rect x="5.5" y="3.8" width="5" height="8.4" rx="1" fill="none" stroke="#fff" stroke-width="1.1"/></svg>
    </li>
    <li class="contact-item">(956)555-0178
      <svg class="contact-icon" viewBox="0 0 16 16"><circle cx="8" cy="8" r="7" fill="none" stroke="#fff" stroke-width="1.2"/><path d="M5.3 4.5 L6.8 4.3 L7.4 6.2 L6.5 7 Q7.3 8.8 9 9.5 L9.8 8.6 L11.7 9.2 L11.5 10.7 Q7 11.2 5.3 4.5 Z" fill="#fff"/></svg>
    </li>
    <li class="contact-item">marcustellwright@heronfreightlines.example
      <svg class="contact-icon" viewBox="0 0 16 16"><circle cx="8" cy="8" r="7" fill="none" stroke="#fff" stroke-width="1.2"/><rect x="4.3" y="5.3" width="7.4" height="5.4" fill="none" stroke="#fff" stroke-width="1"/><path d="M4.3 5.3 L8 8.3 L11.7 5.3" fill="none" stroke="#fff" stroke-width="1"/></svg>
    </li>
    <li class="contact-item">www.heronfreightlines.example
      <svg class="contact-icon" viewBox="0 0 16 16"><circle cx="8" cy="8" r="7" fill="none" stroke="#fff" stroke-width="1.2"/><circle cx="8" cy="8" r="4" fill="none" stroke="#fff" stroke-width="1"/><path d="M4 8 H12 M8 4 Q5.8 8 8 12 Q10.2 8 8 4" fill="none" stroke="#fff" stroke-width="0.9"/></svg>
    </li>
  </ul>
</section>

<section class="card card-back" aria-label="Business card back">
  <div class="wordmark"><span class="wordmark-dot"></span>Heron Freightlines</div>
  <p class="back-web">www.heronfreightlines.example</p>
</section>

</body>
</html>
```